Brightwell Giving Inc

We need a full re-design of our non-profit organization website (www.brightwellgiving.org). Ideally, we are looking to make it more attractive, user-friendly, and interactive with our business model.

Please make sure to user colors that ago with our logo.

We need a homepage done and we also need a content page done where we will use for the other pages to fill with content.

Target Market(s)

Clothes/textiles donations.

Industry/Entity Type

Charity

Number of Pages Required

2 page

Colors

Designer to choose colors to be used in the design.

Requirements
Must have
• It must match the styling of our logo and same colors as current website. (www.brightwellgiving.org)
Nice to have
• Sleek homepage that is easy to understand and get our main points across.

```html
<!DOCTYPE html>
<html lang="en">
<head>
<meta charset="utf-8">
<title>Brightwell Giving — Home</title>
<link href="https://fonts.googleapis.com/css2?family=Roboto+Condensed:wght@400;700&family=Open+Sans:wght@400;600;700&display=swap" rel="stylesheet">
<style>
:root{
  --yellow:#ffd400;
  --yellow-dark:#f3b800;
  --green:#3f7d1e;
  --red:#e3242f;
  --ink:#1d1d1d;
  --text:#555;
  --muted:#8a8a8a;
  --panel:#ececec;
  --footer:#2e2e2e;
  --white:#fff;
}
*{box-sizing:border-box;margin:0;padding:0}
html,body{width:1200px;height:2459px;overflow:hidden;background:var(--white)}
body{font-family:"Open Sans",Arial,sans-serif;color:var(--text);position:relative}
.page{position:relative;width:1200px;height:2459px;overflow:hidden}
.abs{position:absolute}
.cond{font-family:"Roboto Condensed","Arial Narrow",sans-serif}

/* header */
.brand{left:230px;top:20px;display:flex;align-items:center;gap:8px}
.brand-mark{width:30px;height:30px;background:var(--green);border-radius:50%}
.brand-name{font-family:"Roboto Condensed",sans-serif;font-weight:700;font-size:20px;color:var(--green);line-height:1}
.brand-tag{font-size:9px;color:var(--ink);margin-top:2px}
.contact{top:24px;display:flex;align-items:center;gap:8px;font-size:11px;color:var(--ink)}
.contact .ico{width:20px;height:20px;background:var(--red);border-radius:3px;display:flex;align-items:center;justify-content:center}
.btn-donate-top{left:851px;top:21px;width:117px;height:28px;background:var(--red);border-radius:14px;color:#fff;font-size:10px;font-weight:700;display:flex;align-items:center;justify-content:center}
.nav{left:230px;top:69px;width:739px;height:41px;background:linear-gradient(var(--yellow),#f6c600);display:flex;align-items:center;justify-content:space-around;padding:0 20px;z-index:3}
.nav a{font-family:"Roboto Condensed",sans-serif;font-size:11px;font-weight:700;color:#fff;text-decoration:none;text-transform:uppercase}
.nav a.active{color:var(--ink)}

/* hero */
.hero{left:0;top:87px;width:1200px;height:575px;background:linear-gradient(100deg,#f2efeb 0%,#e9e3dc 30%,#d8cdc2 55%,#c9c0b6 75%,#e8e6e2 100%)}
.hero-title{left:230px;top:282px;font-family:"Roboto Condensed",sans-serif;font-weight:700;font-size:50px;line-height:56px;color:var(--ink)}
.hero-text{left:230px;top:408px;width:520px;font-size:13px;font-weight:600;line-height:20px;color:var(--ink)}
.btn{border-radius:17px;font-size:10px;font-weight:700;display:flex;align-items:center;justify-content:center;text-transform:uppercase}
.btn-yellow{background:var(--yellow);color:var(--ink)}
.btn-green{background:var(--green);color:#fff}
.arrow{top:364px;width:50px;height:44px;background:rgba(255,255,255,.85);border:1px solid #555;display:flex;align-items:center;justify-content:center}

/* section headings */
.sec-title{width:1200px;left:0;text-align:center;font-family:"Roboto Condensed",sans-serif;font-weight:700;font-size:20px;color:var(--ink)}
.sec-sub{width:1200px;left:0;text-align:center;font-size:9.5px;line-height:15px;color:var(--ink)}
.divider{left:575px;width:50px;height:2px;background:var(--green)}
.divider::before,.divider::after{content:"";position:absolute;top:-3px;width:2px;height:8px;background:var(--green)}
.divider::before{left:0}.divider::after{right:0}

/* steps */
.step{top:806px;width:186px;height:97px;color:#fff;text-align:center;font-family:"Roboto Condensed",sans-serif;font-weight:700;font-size:11px;line-height:16px;padding:52px 12px 0;text-transform:uppercase}
.step svg{position:absolute;top:12px;left:78px}
.step-green{left:308px;background:var(--green)}
.step-yellow{left:506px;background:var(--yellow)}
.step-red{left:705px;background:var(--red)}
.joint{top:848px;width:14px;height:14px;border-radius:50%;background:#fff}

/* mission */
.mission-panel{left:0;top:964px;width:598px;height:357px;background:var(--panel)}
.mission-photo{left:598px;top:964px;width:602px;height:357px;background:linear-gradient(135deg,#eef0f0,#d9dcdb 45%,#b9a98f 75%,#cfcac2)}
.mission-rule{left:0;top:1022px;width:216px;height:1px;background:var(--ink)}
.mission-title{left:230px;top:1011px;font-family:"Roboto Condensed",sans-serif;font-weight:700;font-size:18px;color:var(--ink)}
.mission-text{left:230px;top:1054px;width:315px;font-size:10.5px;line-height:20.5px;color:var(--text)}

/* donate */
.donate-bg{left:0;top:1321px;width:1200px;height:428px;background:linear-gradient(180deg,#5b6a4a,#4a4f45 50%,#3f3f3d)}
.donate-title{color:#fff}
.level{top:1508px;width:230px;height:123px;background:#fff;text-align:center}
.level-2{background:var(--red);top:1500px;height:139px}
.level h3{font-family:"Roboto Condensed",sans-serif;font-size:19px;font-weight:700;color:var(--ink);margin-top:22px}
.level-2 h3{color:#fff;margin-top:30px}
.amount{margin:12px auto 0;width:162px;height:43px;background:#fff;border:3px solid #d4d4d4;box-shadow:0 2px 3px rgba(0,0,0,.25);display:flex;align-items:center;justify-content:center;font-family:"Roboto Condensed",sans-serif;font-weight:700;font-size:18px;color:var(--red)}
.dot{top:1678px;width:5px;height:5px;border-radius:50%;background:#fff}

/* news */
.news{top:1906px;width:235px}
.news-img{width:235px;height:138px}
.news h4{margin-top:23px;font-family:"Roboto Condensed",sans-serif;font-size:10.5px;font-weight:700;line-height:16px;color:var(--ink);text-transform:uppercase;height:36px}
.meta{margin-top:6px;display:flex;gap:14px;font-size:9px;color:var(--red);font-weight:600}
.meta span{display:flex;align-items:center;gap:5px}
.news p{margin-top:9px;font-size:10px;line-height:17px;color:var(--muted);height:34px}
.news hr{border:0;border-top:1px solid #ddd;margin-top:6px}
.more{margin-top:10px;font-size:9.5px;font-weight:700;color:var(--ink);display:flex;align-items:center;gap:5px}

/* footer */
.footer{left:0;top:2249px;width:1200px;height:210px;background:var(--footer);color:#fff}
.f-title{font-family:"Roboto Condensed",sans-serif;font-weight:700;font-size:14px;color:#fff}
.f-line{height:2px;width:128px;background:var(--yellow)}
.social{width:23px;height:23px;border-radius:50%;background:var(--yellow)}
.f-small{font-size:9.5px;line-height:15px;color:#fff}
.f-row{display:flex;align-items:flex-start;gap:12px}
.f-links a{display:block;font-size:9.5px;line-height:19px;color:#fff;text-decoration:none}
</style>
</head>
<body>
<div class="page">

  <!-- header -->
  <div class="abs brand">
    <div class="brand-mark"></div>
    <div><div class="brand-name">BRIGHTWELL GIVING</div><div class="brand-tag">Think Globally while Donating Locally</div></div>
  </div>
  <div class="abs contact" style="left:492px">
    <span class="ico"><svg width="11" height="11" viewBox="0 0 24 24"><path fill="#fff" d="M6.6 10.8a15.1 15.1 0 0 0 6.6 6.6l2.2-2.2c.3-.3.7-.4 1-.2 1.1.4 2.3.6 3.6.6.6 0 1 .4 1 1V20c0 .6-.4 1-1 1A17 17 0 0 1 3 4c0-.6.4-1 1-1h3.5c.6 0 1 .4 1 1 0 1.3.2 2.5.6 3.6.1.3 0 .7-.2 1z"/></svg></span>
    <span>CAll : (855) 410-3862</span>
  </div>
  <div class="abs contact" style="left:628px">
    <span class="ico"><svg width="11" height="9" viewBox="0 0 22 16"><rect x="1" y="1" width="20" height="14" fill="none" stroke="#fff" stroke-width="2"/><path d="M1 1l10 8 10-8" fill="none" stroke="#fff" stroke-width="2"/></svg></span>
    <span>E-mail : info@brightwellgiving.org</span>
  </div>
  <div class="abs btn-donate-top">DONATE NOW</div>

  <nav class="abs nav">
    <a class="active">Home</a><a>Missions</a><a>How it works</a><a>About us</a><a>Sponsors</a><a>News</a><a>Donate</a><a>Wall of needs</a>
  </nav>

  <!-- hero -->
  <div class="abs hero" role="img" aria-label="Photo of smiling volunteers sorting donated clothing into boxes, with a child holding a thank-you sign"></div>
  <h1 class="abs hero-title">WE ARE AN OPEN BOOK<br>ORGANIZATION</h1>
  <p class="abs hero-text">Brightwell Giving is a non-profit organization that was created for one purpose: helping the less fortunate in our country’s time of greatest need.</p>
  <div class="abs btn btn-yellow" style="left:230px;top:472px;width:120px;height:33px">Learn more</div>
  <div class="abs arrow" style="left:0"><svg width="18" height="12" viewBox="0 0 18 12"><path d="M17 6H3M7 1L2 6l5 5" stroke="#222" stroke-width="2" fill="none"/></svg></div>
  <div class="abs arrow" style="left:1150px"><svg width="18" height="12" viewBox="0 0 18 12"><path d="M1 6h14M11 1l5 5-5 5" stroke="#222" stroke-width="2" fill="none"/></svg></div>

  <!-- how it works -->
  <h2 class="abs sec-title" style="top:712px">HOW IT WORKS</h2>
  <p class="abs sec-sub" style="top:743px">Brightwell Giving is particularly qualified to assure an effort for<br>an outstanding clothing recovery initiative</p>
  <div class="abs divider" style="top:779px"></div>

  <div class="abs step step-green">
    <svg width="30" height="30" viewBox="0 0 30 30"><rect x="3" y="10" width="24" height="16" fill="none" stroke="#fff" stroke-width="2"/><path d="M3 10l5-6h14l5 6" fill="none" stroke="#fff" stroke-width="2"/></svg>
    Drop off clothing at your closest donation bin</div>
  <div class="abs step step-yellow">
    <svg width="30" height="30" viewBox="0 0 30 30"><rect x="14" y="14" width="13" height="12" fill="none" stroke="#fff" stroke-width="2"/><path d="M15 20h12M20 14v12" stroke="#fff" stroke-width="2"/></svg>
    We pick it up and take it to our sorting facility</div>
  <div class="abs step step-red">
    <svg width="30" height="30" viewBox="0 0 30 30"><path d="M3 22h8l6 3 10-6-2-2-7 3h-6" fill="none" stroke="#fff" stroke-width="2"/><path d="M20 13c-4-3-6-5-6-7a3 3 0 0 1 6-1 3 3 0 0 1 6 1c0 2-2 4-6 7z" fill="#fff"/></svg>
    Charities get clothing. We pay you for the clothes</div>
  <div class="abs joint" style="left:491px"></div>
  <div class="abs joint" style="left:690px"></div>

  <!-- mission -->
  <div class="abs mission-panel"></div>
  <div class="abs mission-photo" role="img" aria-label="Photo of volunteers packing donated clothes into cardboard boxes in a bright hall"></div>
  <div class="abs mission-rule"></div>
  <h2 class="abs mission-title">MISSION</h2>
  <p class="abs mission-text">Brightwell Giving has a two part mission to help local communities while helping the planet. The average American discards 68 lbs of clothing annually. That is 1,325,340,196 lbs for New York State alone and 21,202,400,000 lbs for the U.S. every year! By keeping unwanted clothes out of the trash can we are greatly reducing the amount of material that enters our landfills. We are also turning the unwanted clothes into funding for our local communities. We are asking for your help to increase local support.</p>
  <div class="abs btn btn-yellow" style="left:230px;top:1246px;width:105px;height:29px">Learn more</div>
  <div class="abs btn btn-green" style="left:346px;top:1246px;width:107px;height:29px">Donate now</div>

  <!-- donate -->
  <div class="abs donate-bg" role="img" aria-label="Photo of smiling volunteers working together outdoors, darkened"></div>
  <h2 class="abs sec-title donate-title" style="top:1386px;color:#fff">DONATE NOW</h2>
  <p class="abs sec-sub" style="top:1414px;color:#fff">Thank you for your big heart<br>God Bless You!</p>
  <div class="abs divider" style="top:1451px;background:#fff"></div>

  <div class="abs level" style="left:257px"><h3>LEVEL 1</h3><div class="amount">$1000</div></div>
  <div class="abs level" style="left:716px"><h3>LEVEL 3</h3><div class="amount">$2500 - 5000</div></div>
  <div class="abs level level-2" style="left:487px"><h3>LEVEL 2</h3><div class="amount">$1000 - 2500</div></div>
  <div class="abs dot" style="left:595px"></div>
  <div class="abs dot" style="left:603px"></div>

  <!-- recent news -->
  <h2 class="abs sec-title" style="top:1800px">RECENT NEWS</h2>
  <p class="abs sec-sub" style="top:1830px">Brightwell Giving is particularly qualified to assure an effort for<br>an outstanding clothing recovery initiative</p>
  <div class="abs divider" style="top:1867px"></div>

  <article class="abs news" style="left:230px">
    <div class="news-img" role="img" aria-label="Photo of volunteers handing out flyers and donation boxes" style="background:linear-gradient(135deg,#8ba96a,#c7b08e 55%,#e5dccd)"></div>
    <h4>Brightwell Giving created the flyer for inform the people in Manhattan to help...</h4>
    <div class="meta"><span><svg width="10" height="10" viewBox="0 0 10 10"><rect x=".5" y="1.5" width="9" height="8" fill="none" stroke="#e3242f"/><path d="M.5 4h9" stroke="#e3242f"/></svg>Date : 22 march-18</span><span><svg width="10" height="10" viewBox="0 0 10 10"><circle cx="5" cy="3" r="2.3" fill="#e3242f"/><path d="M0 10a5 5 0 0 1 10 0z" fill="#e3242f"/></svg>By Admin</span></div>
    <p>Brightwell Giving created the flyer for inform the people in Manhattan to help others..</p>
    <hr><div class="more">LEARN MORE <svg width="9" height="7" viewBox="0 0 9 7"><path d="M0 3.5h7M5 1l2.5 2.5L5 6" stroke="#222" fill="none"/></svg></div>
  </article>

  <article class="abs news" style="left:482px">
    <div class="news-img" role="img" aria-label="Photo of a group of volunteers holding donation boxes" style="background:linear-gradient(135deg,#86b2d8,#c8b88c 55%,#9fb26c)"></div>
    <h4>Charity project Love Thy Neighbor donation boxes</h4>
    <div class="meta"><span><svg width="10" height="10" viewBox="0 0 10 10"><rect x=".5" y="1.5" width="9" height="8" fill="none" stroke="#e3242f"/><path d="M.5 4h9" stroke="#e3242f"/></svg>Date : 22 march-18</span><span><svg width="10" height="10" viewBox="0 0 10 10"><circle cx="5" cy="3" r="2.3" fill="#e3242f"/><path d="M0 10a5 5 0 0 1 10 0z" fill="#e3242f"/></svg>By Admin</span></div>
    <p>Started Charitable project LOVE THY NEIGHBOR donation boxes. Brightwell Giving team ...</p>
    <hr><div class="more">LEARN MORE <svg width="9" height="7" viewBox="0 0 9 7"><path d="M0 3.5h7M5 1l2.5 2.5L5 6" stroke="#222" fill="none"/></svg></div>
  </article>

  <article class="abs news" style="left:734px">
    <div class="news-img" role="img" aria-label="Photo of a thrift store storefront during a ribbon-cutting opening" style="background:linear-gradient(180deg,#4d6b8a,#7b8796 45%,#b9a47a)"></div>
    <h4>We are starting the charity projects to collect funds on FundCircle</h4>
    <div class="meta"><span><svg width="10" height="10" viewBox="0 0 10 10"><rect x=".5" y="1.5" width="9" height="8" fill="none" stroke="#e3242f"/><path d="M.5 4h9" stroke="#e3242f"/></svg>Date : 22 march-18</span><span><svg width="10" height="10" viewBox="0 0 10 10"><circle cx="5" cy="3" r="2.3" fill="#e3242f"/><path d="M0 10a5 5 0 0 1 10 0z" fill="#e3242f"/></svg>By Admin</span></div>
    <p>April 1, 2017: We opened our first location in Manhattan to sell clothes on the streets of New York.</p>
    <hr><div class="more">LEARN MORE <svg width="9" height="7" viewBox="0 0 9 7"><path d="M0 3.5h7M5 1l2.5 2.5L5 6" stroke="#222" fill="none"/></svg></div>
  </article>

  <!-- footer -->
  <footer class="abs footer">
    <div class="abs f-title" style="left:230px;top:52px">BRIGHTWELL GIVING</div>
    <div class="abs" style="left:230px;top:86px;display:flex;gap:11px">
      <span class="social"></span><span class="social"></span><span class="social"></span><span class="social"></span>
    </div>
    <div class="abs f-small" style="left:230px;top:121px">© Copyright 2018 brightwellgiving.<br>All Rights Reserved.</div>

    <div class="abs f-title" style="left:454px;top:46px">Keep in Touch</div>
    <div class="abs f-line" style="left:454px;top:71px"></div>
    <div class="abs f-row f-small" style="left:454px;top:92px"><svg width="11" height="11" viewBox="0 0 24 24"><path fill="#ffd400" d="M6.6 10.8a15.1 15.1 0 0 0 6.6 6.6l2.2-2.2c.3-.3.7-.4 1-.2 1.1.4 2.3.6 3.6.6.6 0 1 .4 1 1V20c0 .6-.4 1-1 1A17 17 0 0 1 3 4c0-.6.4-1 1-1h3.5c.6 0 1 .4 1 1 0 1.3.2 2.5.6 3.6.1.3 0 .7-.2 1z"/></svg><span>(855) 410-3862</span></div>
    <div class="abs f-row f-small" style="left:454px;top:117px"><svg width="11" height="14" viewBox="0 0 12 16"><path fill="#ffd400" d="M6 0a6 6 0 0 1 6 6c0 4-6 10-6 10S0 10 0 6a6 6 0 0 1 6-6zm0 3.5a2.5 2.5 0 1 0 0 5 2.5 2.5 0 0 0 0-5z"/></svg><span>Lorem Ipsum is simply dummy text<br>of the printing</span></div>
    <div class="abs f-row f-small" style="left:454px;top:158px"><svg width="12" height="10" viewBox="0 0 22 16"><rect x="1" y="1" width="20" height="14" fill="#ffd400"/><path d="M1 1l10 8 10-8" fill="none" stroke="#2e2e2e" stroke-width="2"/></svg><span>info@brightwellgiving.org</span></div>

    <div class="abs f-title" style="left:716px;top:46px">Quick Links</div>
    <div class="abs f-line" style="left:716px;top:71px;width:102px"></div>
    <div class="abs f-links" style="left:716px;top:87px"><a>Home</a><a>Missions</a><a>How it works</a><a>About Us</a><a>Sponsors</a></div>
    <div class="abs f-links" style="left:908px;top:87px"><a>News</a><a>Donate</a><a>Wall of needs</a><a>Help</a></div>
  </footer>

</div>
</body>
</html>
```